Sassy Funky Web Design Project

NOTE: PAYMENT IS GUARANTEED for this project :)

++++++++++++++++++

I meant to share with you my mission for Caring Summit:

To inspire nurses to take action that impacts change in their lives, their organizations, or even the world.

Values:
I – Integrity
M – Mentoring / Motivation
P – Passion for excellence
A – Accountability
C – Competence / knowledge/ achievement
T – Transformation – positive change

++++++++++++++++++

This is a Membership site so will need to show 'Members Login' etc.

Please make sure you use SUPER HIGH QUALITY PHOTOGRAPHY / IMAGES :)

This is a WORDPRESS site for my client - here's some questions I asked her with her answers:

1. Why do you want a website (or have your current site redesigned)?

I want a website to generate income, and residual income, promote quality education material to professionals that is not the same on-line programs point and click to answer questions. I want an interactive way to make a impact in nursing hence CaringSUMMIT.

2. What’s your business/organization all about?

My parent company is Verity Brook Partners, LLC. I started it in 2001 and I provide consultative services to the legal and medical professionals. Mostly legal professionals; attorneys, and offer expert witness testimony. I also present full-day seminars regarding legal aspects of healthcare for nurses and hospital executive leaders. I am always promoting the professionalism in nursing where ever I can.

3. What sets your business apart from your competition?

What I will offer is instant access to quality and reliable clinical information and reliable business support for legal nurse consultants. I have not found another website that offers videos of clinical skills that nurses can watch over and over again without paying a lot of money for. Most of the information for nurses is through online learning read a packet, answer questions, and hopefully, maybe, they learned something. One of the reasons why my seminars are so well attended is they are interactive, and I use real examples to act out scenarios. I want nurses to be able to access short 7-10 minute video/podcasts that will show them how things are done and not just reading about it. Assessment skills will be performed on my family members in a clinic setting to create a realistic view. I want these to be somehow interactive if possible to reinforce the learning. Maybe you have some ideas on that.

For the legal nurse consultants. The programs are driving the “certification” outcome. When the nurses complete these programs, they have no experience and therefore are not able to recover their investment. I want to provide for them the same type of visual education support as the clinical nurses. These two audiences do not have to be mutually exclusive because they do tend to overlap in the real world.

I provide personal mentoring for novice legal nurse consultants in one week programs to support the application need in the LNC community. These weeks are valuable to the novice LNC trying to get started.

4. What problems does your business solve?

Application of concepts which is where I came up with Verity Brook Partners. I also have a tag with CaringSUMMIT I have used: Education, training, application. I put the theory into practice. I translate the pages to the living people.

5. Who are your prospective customers or visitors?

Customers:
Nurses, Advanced Practice Nurses, Legal Nurse Consultants, Attorneys for the clinical/medical information, Universities that offer nursing programs,
Nursing students (I really want to pursue this niche, perhaps a discount for enrolled students???)

Visitors:
Hospital Chief Nursing Officers, Attorneys, Long Term Care Administrators, Faculty of Nursing programs.

6. What do you NOT want on your website?

A flat appearing, boxy, traditional site. I want the nurses to be able to navigate through without much effort, remember many are technologically challenged….
NOooo cartoons… not too many stock photos, I would rather take real images if at all possible to keep the site “alive and real”.

What do you like?

QRV.tv: the listing of videos is going to be important in my site because I will be making clinical example videos and interview videos that can be viewed over and over again by the Platinum members. I plan to have a blog and many downloads available as well.

Tovamesh.com: I like the layout but I do want more interaction with mine. I do like the are you a training leader? Department leader: emerging leader? Componenets because I am addressing Nurses, Nurse Leaders, Legal Nurse Consultants… this would be important to establish right up front. I particularly like the video enhanced special report the new prospect has access to. I will do this for my site. I think it is also cool that you can change the color of the landing page to your liking.

www.thebrindlecove.com: I like a lot of things on this website but it is a bit difficult to navigate for even me. I like the short one minute capture of audio cds. I do plan to have CD material available. I do like the what you get with each level of membership under brindlelink tab. Some of the pages are not easy to read because the color is too dark and the font color is not contrasted enough. I like the tips in ten downloads on CD as well. I can see this working with mine as similar formatting with of course difference content.

www.ginaforsby.org: I do like the section she has on photo gallery where I can post event that have taken place as I speak, and work one-on-one with nurses across the country. (not the fashion shoot ?).

www.7horizons.com: I love the rollover interaction, the eyes constantly moving to the movement across the site.
http://www.dorvesta.org/DorvestaMultimedia.aspx?VideoId=8830461729004&type=M Quick lane video using sketchpad is a cool idea.

www.pebblevault.com - nice and clean

11. Please give us a list of websites that you DON’T Like and Why you Don’t like them.

www.lurn.com: landing page is way too crowded, too many colors, I don’t know where to go for what I would be looking for. Font is too small with large amounts of content.

www.casewardhub.com: this site is way too busy and difficult to navigate however I do like the page titled: Memorable BRWP cases. I would use a page like this for memorable Caring Summit experiences that would encourage others and remember the great things nurses do.

www.wardskills.com: Do not like at all. Way to juvenile.

Colour Scheme:

The colors palette I like is…. I think you will get the general idea of the color scheme. I like the yellow on dark colors so it pops, make sense?

F7C40E
4819A9
2E1FAC
F7D80E
Updates

Payment is guaranteed for this project now! :)

Thank you

Target Market(s)

Customers: Nurses, Advanced Practice Nurses, Legal Nurse Consultants, Attorneys for the clinical/medical information, Universities that offer nursing

Values:
I – Integrity
A – Accountability

Industry/Entity Type

Healthcare

Requirements
Must have
• professional, clean, VERY HIGH QUALITY IMAGES/ PHOTOGRAPHY e.g. PixQuarry
Nice to have
• Brock:
I have shown the design template to several people to get their first impression. I was shocked. They thought of the Tacoma Riveters! The football team. Ouch. I don’t want that. Crazy what others see.
Can we please change the color scheme to incorporate the colors below with the same layout. The Layout is good, it is the color I need to work a bit more on. Sorry about this but I don’t want to be a Riveters fan.

336699
FFCC66
FFFFFF
003366

Yvonne

New logo required: Caring Summit - DO NOT USE MEDICAL
Should not have
• childish graphics, or icons.
Don't want to see unprofessional site with clumsy type or template type designs. We can include some photos.

```html
<!DOCTYPE html>
<html lang="en">
<head>
<meta charset="utf-8">
<title>Caring Summit – Contact us</title>
<link rel="stylesheet" href="https://fonts.googleapis.com/css2?family=PT+Sans:wght@400;700&family=Arimo:wght@400;600;700&display=swap">
<style>
  :root {
    --ink: #333333;
    --muted: #888888;
    --yellow: #f7c40e;
    --yellow-light: #f9d838;
    --yellow-edge: #e4ae00;
    --nav-divider: #d9a800;
    --purple: #5a2fb8;
    --purple-deep: #4819a9;
    --footer-top: #2e2e2e;
    --footer-bottom: #000000;
    --panel-grey: #dedede;
    --white: #ffffff;
  }
  * { box-sizing: border-box; margin: 0; padding: 0; }
  html, body { width: 1200px; height: 1135px; overflow: hidden; background: var(--white); }
  body { position: relative; font-family: "PT Sans", Arial, sans-serif; color: var(--ink); }
  .abs { position: absolute; }

  .top-bar { left: 0; top: 0; width: 1200px; height: 7px; background: #2b2b2b; }
  .utility-links { right: 48px; top: 18px; font-family: "Arimo", Arial, sans-serif; font-size: 15px; color: var(--ink); }
  .utility-links .sep { margin: 0 8px; }

  .brand { left: 40px; top: 66px; display: flex; align-items: center; gap: 12px; }
  .brand-mark { width: 22px; height: 22px; background: var(--yellow); }
  .brand-name { font-family: "Arimo", Arial, sans-serif; font-weight: 600; font-size: 30px; color: #4a4a4a; }

  .search { left: 869px; top: 94px; width: 286px; height: 36px; border: 1px solid #bdbdbd; border-radius: 5px; background: linear-gradient(#f7f7f7, #ececec); }
  .search-text { left: 12px; top: 8px; font-style: italic; font-size: 15px; color: #555; }
  .search svg { position: absolute; right: 8px; top: 7px; }

  .main-nav { left: 0; top: 155px; width: 1200px; height: 56px; background: linear-gradient(var(--yellow-light), var(--yellow)); border-bottom: 2px solid var(--yellow-edge); }
  .main-nav a { position: absolute; top: 18px; font-family: "Arimo", Arial, sans-serif; font-weight: 600; font-size: 16px; color: #3a3a3a; text-decoration: none; }
  .nav-divider { position: absolute; top: 0; width: 1px; height: 56px; background: var(--nav-divider); }

  .page-title { left: 40px; top: 244px; display: flex; align-items: center; gap: 4px; font-size: 24px; font-weight: 400; color: #222; }
  .intro { left: 51px; top: 305px; font-size: 16px; color: var(--muted); }
  .field-label { left: 52px; font-size: 16px; color: #444; }
  .field { left: 51px; width: 329px; height: 26px; border: 1px solid #a9a9a9; background: var(--white); }
  .submit-query { left: 242px; top: 725px; width: 136px; height: 28px; background: var(--yellow); border-radius: 4px; font-family: "PT Sans", Arial, sans-serif; font-weight: 700; font-size: 14px; color: #222; text-align: center; line-height: 28px; }
  .column-divider { left: 493px; top: 295px; width: 1px; height: 446px; background: linear-gradient(transparent, #7d6fc4 15%, #7d6fc4 85%, transparent); }

  .email-graphic { left: 1056px; top: 232px; width: 72px; height: 68px; border-radius: 50%; background: radial-gradient(circle at 40% 40%, #7da2c9, #2f5d8f); }
  .map { left: 598px; top: 376px; width: 292px; height: 291px; border: 1px solid #c9c9c9; background: linear-gradient(135deg, #ebe7df, #ddd8cc 55%, #f1e79a); }

  .contact-heading { left: 931px; top: 524px; display: flex; align-items: center; gap: 15px; font-family: "Arimo", Arial, sans-serif; font-size: 21px; color: #555; }
  .contact-lines { left: 935px; top: 568px; font-size: 15px; color: #444; line-height: 28px; }

  .site-footer { left: 0; top: 792px; width: 1200px; height: 343px; background: linear-gradient(var(--footer-top), #111 50%, var(--footer-bottom)); color: var(--white); }
  .footer-col { top: 20px; }
  .footer-col h3 { font-size: 19px; font-weight: 700; margin-bottom: 18px; }
  .footer-col li { list-style: none; font-size: 14px; font-weight: 700; line-height: 29px; }
  .newsletter-title { left: 704px; top: 16px; font-size: 19px; font-weight: 700; }
  .newsletter { left: 696px; top: 48px; width: 454px; height: 179px; border-radius: 3px; overflow: hidden; background: var(--panel-grey); }
  .newsletter-head { height: 37px; background: var(--purple); font-size: 15px; line-height: 37px; padding-left: 9px; }
  .newsletter-body { color: #222; font-size: 15px; line-height: 29px; padding: 7px 10px 0; }
  .newsletter-input { left: 11px; top: 107px; width: 291px; height: 33px; border: 1px solid #9b9b9b; border-radius: 4px; background: #e9e9e9; font-size: 13px; color: #999; line-height: 31px; padding-left: 10px; }
  .newsletter-submit { left: 338px; top: 107px; width: 95px; height: 32px; border-radius: 4px; background: var(--yellow); color: #222; font-size: 16px; text-align: center; line-height: 32px; box-shadow: 0 3px 4px rgba(0,0,0,.25); }
  .newsletter-foot { left: 0; top: 149px; width: 454px; height: 30px; background: var(--purple); font-size: 15px; line-height: 30px; padding-left: 14px; }
  .social { top: 246px; width: 46px; height: 46px; border-radius: 50%; background: radial-gradient(circle at 50% 35%, #ffffff, #cfcfcf); }
  .footer-rule { left: 35px; top: 301px; width: 1121px; height: 1px; background: #6a6a6a; }
  .copyright { left: 39px; top: 309px; font-size: 14px; font-weight: 700; }
</style>
</head>
<body>
  <div class="abs top-bar"></div>

  <div class="abs utility-links">Member Login<span class="sep">|</span>Client<span class="sep">|</span>Support<span class="sep">|</span>FAQ</div>

  <div class="abs brand">
    <span class="brand-mark"></span>
    <span class="brand-name">Caring Summit</span>
  </div>

  <div class="abs search">
    <span class="abs search-text">Search here</span>
    <svg width="24" height="22" viewBox="0 0 24 22" aria-hidden="true"><circle cx="9" cy="9" r="7" fill="none" stroke="#111" stroke-width="2.5"/><line x1="14" y1="14" x2="22" y2="20" stroke="#111" stroke-width="3" stroke-linecap="round"/></svg>
  </div>

  <nav class="abs main-nav">
    <a style="left:58px">Main</a>
    <span class="nav-divider" style="left:122px"></span>
    <a style="left:148px">About Company</a>
    <span class="nav-divider" style="left:295px"></span>
    <a style="left:325px">Services</a>
    <span class="nav-divider" style="left:412px"></span>
    <a style="left:445px">Seminars</a>
    <span class="nav-divider" style="left:540px"></span>
    <a style="left:571px">Blog</a>
    <span class="nav-divider" style="left:632px"></span>
    <a style="left:660px">Member Login</a>
    <span class="nav-divider" style="left:793px"></span>
    <a style="left:823px">Contact Us</a>
  </nav>

  <h1 class="abs page-title">
    <svg width="44" height="44" viewBox="0 0 44 44" aria-hidden="true"><path d="M6 8 C2 22 10 38 20 40 C28 30 34 18 42 12" fill="none" stroke="#4819a9" stroke-width="3" stroke-linecap="round"/></svg>
    Contact us
  </h1>
  <p class="abs intro">Kindly post your valuable Suggestions &amp;&nbsp; Query</p>

  <span class="abs field-label" style="top:352px">Enter your Name</span>
  <div class="abs field" style="top:382px"></div>
  <span class="abs field-label" style="top:423px">Enter your Email</span>
  <div class="abs field" style="top:453px"></div>
  <span class="abs field-label" style="top:494px">Enter your Phone Number</span>
  <div class="abs field" style="top:524px"></div>
  <span class="abs field-label" style="top:564px">Add your Comments Here</span>
  <div class="abs field" style="top:594px;height:116px"></div>
  <div class="abs submit-query">SUBMIT QUERY</div>

  <div class="abs column-divider"></div>

  <div class="abs email-graphic" role="img" aria-label="Email symbol graphic"></div>
  <div class="abs map" role="img" aria-label="Street map showing the office location"></div>

  <div class="abs contact-heading">
    <svg width="30" height="30" viewBox="0 0 30 30" aria-hidden="true"><rect width="30" height="30" rx="5" fill="#d6d6d6"/><path d="M10 6 C6 8 6 14 10 20 C14 25 19 26 21 23 L19 19 L16 20 C14 18 12 15 12 12 L14 10 Z" fill="#fff"/></svg>
    Contact Details
  </div>
  <div class="abs contact-lines">
    #27 Ferncourt Road,Lorem ipsum,<br>
    Phone: +91 804719235<br>
    Tollfree: (007) 51829364<br>
    E-mail: info@caringsummit.com
  </div>

  <footer class="abs site-footer">
    <div class="abs footer-col" style="left:38px">
      <h3>Company</h3>
      <ul><li>Company</li><li>Media Resources</li><li>Press Releases</li><li>News</li><li>Contact</li></ul>
    </div>
    <div class="abs footer-col" style="left:207px">
      <h3>Why We Are</h3>
      <ul><li>Why Choose Us</li><li>Testimonials</li><li>Recent Blog</li><li>Features</li></ul>
    </div>
    <div class="abs footer-col" style="left:378px">
      <h3>Services</h3>
      <ul><li>Why Choose Us</li><li>Testimonials</li><li>Recent Blog</li><li>Features</li></ul>
    </div>
    <div class="abs footer-col" style="left:541px">
      <h3>Support &amp; FAQ</h3>
      <ul><li>Support</li><li>Blog</li><li>Video</li><li>Support</li></ul>
    </div>

    <div class="abs newsletter-title">Newsletter</div>
    <div class="abs newsletter">
      <div class="newsletter-head">Yvonne C Marlowe-Densby:a Expert Author Email Alerts</div>
      <div class="newsletter-body">Sign up to receive email alerts of Yvonne C Marlowe-DensbyCs latest articles from QuillPost.com!</div>
      <div class="abs newsletter-input">Enter your Email Address</div>
      <div class="abs newsletter-submit">Submit</div>
      <div class="abs newsletter-foot">Lorem ipsum.com</div>
    </div>

    <div class="abs social" style="left:980px" role="img" aria-label="Social link"></div>
    <div class="abs social" style="left:1031px" role="img" aria-label="Social link"></div>
    <div class="abs social" style="left:1084px" role="img" aria-label="Social link"></div>

    <div class="abs footer-rule"></div>
    <div class="abs copyright">© 2012 Company Name&nbsp; |&nbsp; All right reserved</div>
  </footer>
</body>
</html>
```